Flyer for annual KESTREL SUMMIT 2020

I would like a church event flyer designed. The event is called "KESTREL SUMMIT 2020". I am looking for a professional, yet catchy design that uses our brand colors and logo creatively while communicating key information of the event effectively.

1. The logo is attached in two color formats. The designer has the choice to use them as he/she want.

2. The location of the event is: Harlow Community Center, 239 Fennimore Street, Portland, ME 04117

3. Time and date of event. The designer can organize and format the date and time as he/she pleases.
Thursday December 31st @ 6:30PM
Friday January 1st @ 6:30PM
Saturday 2nd @ 6:30PM
Sunday 3rd @ 4:30PM

4. The topic of the event is "In Fire and On Fire". The designer is free to use this phrase as he/she pleases to create a good composition.

5. Speaker: Prophet Marcus Olunde (2 pictures of the speaker to choose from are attached)

6. Contact information: contact@brightmeadowfold.org - Telephone number: 207 583 2914

7. I would also like the following three words on the flyer. These words describe the focus of the event: FIRE, REVIVAL, PROPHETIC

Target Market(s)

Young adults

Font styles to use
Sans Serif

Requirements
Must have
• Logo, speaker's picture
Should not have
• cross image, church image

```html
<!DOCTYPE html>
<html lang="en">
<head>
<meta charset="utf-8">
<title>Kestrel Summit 2020 Flyer</title>
<link href="https://fonts.googleapis.com/css2?family=Barlow+Condensed:wght@500;600;700&family=Barlow:wght@400;500;600&family=Cinzel:wght@500;600&display=swap" rel="stylesheet">
<style>
  :root {
    --ink: #050608;
    --teal-deep: #0d3440;
    --teal-mid: #15505c;
    --silver: #e9ecef;
    --silver-shade: #a9b0b6;
    --sky: #1aa6e6;
    --amber: #f39a1e;
    --white: #ffffff;
  }
  * { margin: 0; padding: 0; box-sizing: border-box; }
  html, body { width: 899px; height: 1200px; overflow: hidden; background: var(--ink); }
  .flyer {
    position: relative; width: 899px; height: 1200px; overflow: hidden;
    background: linear-gradient(180deg, var(--teal-mid) 0%, var(--teal-deep) 30%, #08161b 52%, var(--ink) 72%);
    font-family: "Barlow", sans-serif; color: var(--white);
  }
  .crowd-backdrop {
    position: absolute; left: 0; top: 0; width: 899px; height: 760px;
    background: radial-gradient(ellipse at 60% 35%, rgba(40,110,125,.55), rgba(5,6,8,0) 65%);
  }
  .speaker-photo {
    position: absolute; left: 0; top: 330px; width: 560px; height: 700px;
    background:
      radial-gradient(ellipse 120px 150px at 330px 120px, rgba(70,45,35,.9), rgba(70,45,35,0) 100%),
      radial-gradient(ellipse 260px 330px at 270px 420px, rgba(217,84,42,.95), rgba(160,50,25,.6) 60%, rgba(5,6,8,0) 100%);
  }
  .brand { position: absolute; left: 38px; top: 30px; display: flex; align-items: center; gap: 10px; }
  .brand-dot { width: 20px; height: 20px; border-radius: 50%; background: var(--amber); }
  .brand-name { font-family: "Cinzel", serif; font-weight: 500; font-size: 44px; color: var(--white); letter-spacing: 1px; }

  .event-title { position: absolute; right: 46px; top: 40px; text-align: right; font-family: "Barlow Condensed", sans-serif; font-weight: 600; line-height: 1; white-space: nowrap; }
  .event-title .name { display: block; font-size: 132px; background: linear-gradient(180deg, #fff 0%, var(--silver) 50%, var(--silver-shade) 100%); -webkit-background-clip: text; background-clip: text; -webkit-text-fill-color: transparent; }
  .event-title .kind { display: block; font-size: 100px; color: var(--sky); margin-top: -4px; }
  .event-title .year { display: block; font-size: 88px; color: var(--amber); margin-top: 2px; }

  .theme-rule { position: absolute; left: 524px; width: 329px; height: 7px; background: linear-gradient(180deg, #fff, var(--silver-shade)); }
  .theme-rule.top { top: 410px; }
  .theme-rule.bottom { top: 698px; }
  .theme-line {
    position: absolute; left: 504px; width: 369px; text-align: center; white-space: nowrap;
    font-family: "Barlow Condensed", sans-serif; font-weight: 600; font-size: 126px; line-height: 1;
    background: linear-gradient(180deg, #fff 0%, var(--silver) 55%, var(--silver-shade) 100%);
    -webkit-background-clip: text; background-clip: text; -webkit-text-fill-color: transparent;
  }
  .theme-line.in-fire { top: 416px; }
  .theme-line.on-fire { top: 574px; }
  .theme-joiner { position: absolute; left: 524px; top: 546px; width: 329px; display: flex; align-items: center; gap: 10px; }
  .theme-joiner .bar { flex: 1; height: 6px; background: linear-gradient(180deg, #fff, var(--silver-shade)); }
  .theme-joiner span { font-family: "Barlow Condensed", sans-serif; font-size: 22px; font-weight: 600; }
  .flame { position: absolute; width: 30px; height: 44px; }

  .focus-list { position: absolute; right: 46px; top: 748px; list-style: none; }
  .focus-list li { display: flex; align-items: center; justify-content: flex-end; gap: 18px; height: 64px; font-size: 26px; font-weight: 500; letter-spacing: 8px; }
  .focus-icon { width: 46px; height: 46px; }

  .venue { position: absolute; left: 30px; top: 928px; width: 330px; text-align: center; font-style: normal; }
  .venue-name { font-family: "Cinzel", serif; font-weight: 600; font-size: 40px; line-height: 1; }
  .venue-type { font-family: "Cinzel", serif; font-weight: 500; font-size: 25px; line-height: 1.1; margin-top: 4px; }
  .venue-address { color: var(--sky); font-size: 17px; line-height: 1.2; margin-top: 4px; white-space: nowrap; }

  .contact { position: absolute; left: 41px; top: 1052px; width: 304px; height: 116px; border: 2px solid var(--white); border-radius: 10px; text-align: center; padding-top: 9px; }
  .contact-label { font-size: 21px; letter-spacing: 2px; font-weight: 500; line-height: 1.1; }
  .contact-phone { font-family: "Barlow Condensed", sans-serif; font-weight: 700; font-size: 42px; color: var(--amber); letter-spacing: 3px; line-height: 1.1; }
  .contact-email { font-size: 18px; line-height: 1.2; }

  .schedule { position: absolute; left: 420px; top: 965px; display: flex; font-family: "Barlow Condensed", sans-serif; font-weight: 700; white-space: nowrap; }
  .months { width: 206px; text-align: right; padding-right: 12px; padding-top: 19px; color: var(--sky); font-size: 40px; line-height: 46px; }
  .divider { width: 2px; height: 215px; background: var(--silver-shade); }
  .sessions { list-style: none; padding-left: 14px; padding-top: 19px; font-size: 40px; line-height: 46px; }
  .sessions sup { font-size: 18px; vertical-align: 16px; line-height: 0; }
  .sessions .time { color: var(--amber); }
</style>
</head>
<body>
<main class="flyer">
  <div class="crowd-backdrop" role="img" aria-label="Dim teal-lit worship crowd with raised hands"></div>
  <div class="speaker-photo" role="img" aria-label="Speaker Prophet Marcus Olunde seated in an orange blazer"></div>

  <div class="brand"><span class="brand-dot"></span><span class="brand-name">CALDER</span></div>

  <h1 class="event-title">
    <span class="name">KESTREL</span>
    <span class="kind">SUMMIT</span>
    <span class="year">2020</span>
  </h1>

  <div class="theme-rule top"></div>
  <svg class="flame" style="left:700px;top:372px" viewBox="0 0 34 48"><path d="M17 2C20 14 30 18 30 31a13 13 0 0 1-26 0C4 22 10 18 12 10c2 6 4 8 5 9 2-6 1-12 0-17z" fill="#f39a1e"/><path d="M17 22c3 6 7 8 7 13a7 7 0 0 1-14 0c0-5 5-7 7-13z" fill="#ffd24a"/></svg>
  <div class="theme-line in-fire">IN FIRE</div>
  <div class="theme-joiner"><div class="bar"></div><span>AND</span><div class="bar"></div></div>
  <div class="theme-line on-fire">ON FIRE</div>
  <svg class="flame" style="left:758px;top:572px" viewBox="0 0 34 48"><path d="M17 2C20 14 30 18 30 31a13 13 0 0 1-26 0C4 22 10 18 12 10c2 6 4 8 5 9 2-6 1-12 0-17z" fill="#f39a1e"/><path d="M17 22c3 6 7 8 7 13a7 7 0 0 1-14 0c0-5 5-7 7-13z" fill="#ffd24a"/></svg>
  <div class="theme-rule bottom"></div>

  <ul class="focus-list">
    <li>FIRE
      <svg class="focus-icon" viewBox="0 0 46 46"><circle cx="23" cy="23" r="21" fill="none" stroke="#f39a1e" stroke-width="2.5"/><path d="M23 10c2 7 8 9 8 16a8 8 0 0 1-16 0c0-5 4-7 5-11 1 3 2 4 3 5 1-3 0-7 0-10z" fill="#f39a1e"/></svg></li>
    <li>REVIVAL
      <svg class="focus-icon" viewBox="0 0 46 46"><circle cx="23" cy="23" r="21" fill="none" stroke="#f39a1e" stroke-width="2.5"/><circle cx="25" cy="13" r="3.5" fill="#f39a1e"/><path d="M22 18l6 2-2 8 5 4h-4l-5-4-4 6h-4l5-8z" fill="#f39a1e"/></svg></li>
    <li>PROPHETIC
      <svg class="focus-icon" viewBox="0 0 46 46"><circle cx="23" cy="23" r="21" fill="none" stroke="#f39a1e" stroke-width="2.5"/><path d="M12 20h5l12-7v20l-12-7h-5z" fill="#f39a1e"/><path d="M16 26l2 7h3l-2-7z" fill="#f39a1e"/></svg></li>
  </ul>

  <address class="venue">
    <div class="venue-name">HARLOW</div>
    <div class="venue-type">COMMUNITY CENTER</div>
    <div class="venue-address">239 Fennimore Street, Portland, ME 04117</div>
  </address>

  <div class="contact">
    <div class="contact-label">CONTACT INFORMATION:</div>
    <div class="contact-phone">207 583 2914</div>
    <div class="contact-email">contact@brightmeadowfold.org</div>
  </div>

  <div class="schedule">
    <div class="months">DECEMBER<br>JANUARY</div>
    <div class="divider"></div>
    <ul class="sessions">
      <li>31<sup>ST</sup> @ <span class="time">6:30PM</span></li>
      <li>1<sup>ST</sup> @ <span class="time">6:30PM</span></li>
      <li>2<sup>ND</sup> @ <span class="time">6:30PM</span></li>
      <li>3<sup>rd</sup> @ <span class="time">4:30PM</span></li>
    </ul>
  </div>
</main>
</body>
</html>
```